Christmas Season's Card 2022

Design a Season's Greetings Card 2022 for a law firm.

Targuet: Intenational Clients who are companies.

I attached the law firm's logo.

```html
<!DOCTYPE html>
<html lang="en">
<head>
<meta charset="utf-8">
<title>Season's Greetings Card 2022</title>
<link rel="stylesheet" href="https://fonts.googleapis.com/css2?family=Great+Vibes&family=Montserrat:wght@400;500&family=Cormorant+Garamond:wght@500&display=swap">
<style>
  :root {
    --paper: #fdf4ee;
    --wine: #7b2c3b;
    --crimson: #d43f5f;
    --rose: #e9728a;
    --gold: #d8b27c;
    --gold-soft: #ecd3ac;
    --ink-light: #ffffff;
  }
  * { margin: 0; padding: 0; box-sizing: border-box; }
  html, body { width: 1200px; height: 907px; overflow: hidden; }
  body { background: var(--paper); }
  .card {
    position: relative;
    width: 1200px;
    height: 907px;
    background: var(--paper);
    overflow: hidden;
  }
  .festive-border { position: absolute; border-radius: 50%; }
  .festive-border--top-left {
    left: -80px; top: -90px; width: 520px; height: 300px;
    background: radial-gradient(ellipse at 40% 45%, rgba(212,63,95,.55), rgba(216,178,124,.45) 50%, rgba(253,244,238,0) 72%);
  }
  .festive-border--top-center {
    left: 420px; top: -110px; width: 440px; height: 260px;
    background: radial-gradient(ellipse at 50% 50%, rgba(216,178,124,.6), rgba(201,110,90,.35) 45%, rgba(253,244,238,0) 72%);
  }
  .festive-border--top-right {
    right: -90px; top: -80px; width: 520px; height: 320px;
    background: radial-gradient(ellipse at 55% 45%, rgba(212,63,95,.6), rgba(216,178,124,.45) 48%, rgba(253,244,238,0) 72%);
  }
  .festive-border--left {
    left: -120px; top: 300px; width: 420px; height: 560px;
    background: radial-gradient(ellipse at 45% 50%, rgba(212,63,95,.5), rgba(216,178,124,.5) 45%, rgba(253,244,238,0) 72%);
  }
  .festive-border--bottom-left {
    left: 60px; bottom: -140px; width: 520px; height: 320px;
    background: radial-gradient(ellipse at 50% 45%, rgba(216,178,124,.6), rgba(233,114,138,.35) 45%, rgba(253,244,238,0) 72%);
  }
  .festive-border--right {
    right: -110px; top: 380px; width: 380px; height: 380px;
    background: radial-gradient(ellipse at 50% 50%, rgba(212,63,95,.55), rgba(216,178,124,.35) 45%, rgba(253,244,238,0) 72%);
  }
  .festive-border--bottom-right {
    right: 40px; bottom: -130px; width: 560px; height: 330px;
    background: radial-gradient(ellipse at 50% 45%, rgba(201,130,100,.55), rgba(216,178,124,.45) 45%, rgba(253,244,238,0) 72%);
  }
  .greeting {
    position: absolute;
    left: 0; right: 0; top: 228px;
    text-align: center;
    color: var(--wine);
  }
  .greeting__merry {
    font-family: "Montserrat", sans-serif;
    font-weight: 400;
    font-size: 40px;
    letter-spacing: 14px;
    padding-left: 14px;
    line-height: 1;
  }
  .greeting__christmas {
    font-family: "Great Vibes", cursive;
    font-size: 168px;
    line-height: 1;
    margin-top: 4px;
    margin-left: -20px;
  }
  .greeting__new-year {
    display: inline-block;
    margin-top: 28px;
    width: 456px;
    height: 38px;
    line-height: 38px;
    border-radius: 19px;
    background: var(--wine);
    color: var(--ink-light);
    font-family: "Montserrat", sans-serif;
    font-weight: 500;
    font-size: 21px;
    letter-spacing: 1px;
  }
  .firm-name {
    margin-top: 20px;
    font-family: "Cormorant Garamond", serif;
    font-weight: 500;
    font-size: 34px;
    line-height: 1.05;
    color: var(--wine);
  }
  .firm-name__practice {
    display: block;
    font-size: 15px;
    letter-spacing: 4px;
    margin-top: 4px;
  }
</style>
</head>
<body>
  <main class="card">
    <div class="festive-border festive-border--top-left" role="img" aria-label="Illustrated poinsettia, candy canes and golden pine branches"></div>
    <div class="festive-border festive-border--top-center" role="img" aria-label="Illustrated gift box with ribbon and a lollipop among gold pine sprigs"></div>
    <div class="festive-border festive-border--top-right" role="img" aria-label="Illustrated red gift box, pine cone and berries"></div>
    <div class="festive-border festive-border--left" role="img" aria-label="Illustrated red gift box, ornament, pine cones and golden branches"></div>
    <div class="festive-border festive-border--bottom-left" role="img" aria-label="Illustrated gold ribbon bow, lollipop and stars"></div>
    <div class="festive-border festive-border--right" role="img" aria-label="Illustrated poinsettia flower and candy cane"></div>
    <div class="festive-border festive-border--bottom-right" role="img" aria-label="Illustrated striped gift box, cotton flowers, berries and gold branches"></div>

    <section class="greeting">
      <p class="greeting__merry">MERRY</p>
      <h1 class="greeting__christmas">Christmas</h1>
      <p class="greeting__new-year">AND HAPPY NEW YEAR</p>
      <p class="firm-name">Ibarra Montoya<br>&amp; Quiroga Llano<span class="firm-name__practice">ABOGADOS</span></p>
    </section>
  </main>
</body>
</html>
```